Shine Barn Auto Care Business Card

2 side business card design for an auto detailing business

Target Market(s)

Auto detailing

Contact Information for Business Card

Things included

The business name “Shine Barn Auto Care”
Owen Marchetti
(403)871-2964
Larkwood, Sk

Services offered - complete interior& exterior detail
- paint correction & protection
- ceramic coating
- trim restore
- auto carpet & seat cleaning

Requirements
Must have
• Colours that are in my logo

Services offered

My name Owen Marchetti
403-871-2964
Larkwood, Sk

Not too sure in what order for these ?
Website. Shinebarnautocare.com
Instagram Shinebarnautocare
Email. Shinebarnautoac@mailbox-example.com

```html
<!DOCTYPE html>
<html lang="en">
<head>
<meta charset="utf-8">
<title>Shine Barn Auto Care — Business Card</title>
<link rel="stylesheet" href="https://fonts.googleapis.com/css2?family=Open+Sans:wght@400;600;700&display=swap">
<style>
  :root {
    --backdrop: #2a2a2a;
    --card: #1c1c1d;
    --red: #a8161d;
    --white: #f2f2f2;
    --emboss: #343436;
  }
  * { box-sizing: border-box; margin: 0; padding: 0; }
  html, body {
    width: 1200px; height: 900px; overflow: hidden;
    background: var(--backdrop);
    font-family: "Open Sans", Arial, sans-serif;
  }
  .sheet {
    width: 1200px; height: 900px;
    display: flex; flex-direction: column;
    align-items: center; justify-content: center; gap: 40px;
  }
  .card {
    position: relative;
    width: 680px; height: 388px;
    background: var(--card);
    border-bottom: 9px solid var(--red);
    box-shadow: 0 10px 30px rgba(0,0,0,.45);
    overflow: hidden;
  }

  /* front */
  .brand {
    position: absolute; left: 44px; top: 150px;
    display: flex; align-items: center; gap: 14px;
  }
  .brand-mark {
    width: 46px; height: 46px; border-radius: 50%;
    background: var(--red); flex: none;
  }
  .brand-name {
    font-weight: 700; font-size: 21px; line-height: 1.15;
    letter-spacing: 1.5px; text-transform: uppercase;
    color: var(--white);
  }
  .divider {
    position: absolute; left: 300px; top: 92px;
    width: 2px; height: 200px; background: var(--red);
  }
  .contact {
    position: absolute; left: 326px; right: 24px; top: 98px;
    color: var(--white);
  }
  .contact-name {
    font-weight: 700; font-size: 23px; color: var(--red);
    text-transform: uppercase; letter-spacing: .5px; line-height: 1.1;
  }
  .contact-role { font-size: 16px; margin: 2px 0 12px; }
  .contact-list { list-style: none; }
  .contact-list li {
    display: flex; align-items: center; gap: 9px;
    font-size: 15px; line-height: 1.6; white-space: nowrap;
  }
  .contact-list svg { width: 13px; height: 13px; flex: none; fill: var(--red); }

  /* back */
  .brand-emboss {
    position: absolute; right: 56px; top: 70px;
    display: flex; align-items: center; gap: 16px;
  }
  .brand-emboss .brand-mark {
    width: 70px; height: 70px; background: var(--emboss);
  }
  .brand-emboss .brand-name {
    font-size: 32px; color: var(--emboss); letter-spacing: 2px;
  }
  .services {
    position: absolute; left: 48px; bottom: 56px;
    color: var(--white); font-size: 17px; line-height: 1.45;
  }
  .services .dot { color: var(--red); margin: 0 7px; }
</style>
</head>
<body>
<main class="sheet">

  <section class="card card-front" aria-label="Card front">
    <div class="brand">
      <span class="brand-mark"></span>
      <span class="brand-name">Shine Barn<br>Auto Care</span>
    </div>
    <div class="divider"></div>
    <div class="contact">
      <p class="contact-name">Owen Marchetti</p>
      <p class="contact-role">President</p>
      <ul class="contact-list">
        <li><svg viewBox="0 0 24 24"><path d="M6.6 10.8a15.1 15.1 0 0 0 6.6 6.6l2.2-2.2a1 1 0 0 1 1-.25 11.4 11.4 0 0 0 3.6.57 1 1 0 0 1 1 1V20a1 1 0 0 1-1 1A17 17 0 0 1 3 4a1 1 0 0 1 1-1h3.5a1 1 0 0 1 1 1c0 1.25.2 2.45.57 3.57a1 1 0 0 1-.25 1z"/></svg>403-871-2964</li>
        <li><svg viewBox="0 0 24 24"><path d="M2 5h20v14H2zm2 2v.5l8 5 8-5V7z"/></svg>Shinebarnautoac@mailbox-example.com</li>
        <li><svg viewBox="0 0 24 24"><circle cx="12" cy="12" r="10"/></svg>Shinebarnautocare.com</li>
        <li><svg viewBox="0 0 24 24"><rect x="3" y="3" width="18" height="18" rx="5"/></svg>Shinebarnautocare</li>
        <li><svg viewBox="0 0 24 24"><path d="M12 2a7 7 0 0 0-7 7c0 5 7 13 7 13s7-8 7-13a7 7 0 0 0-7-7zm0 9.5A2.5 2.5 0 1 1 12 6.5a2.5 2.5 0 0 1 0 5z"/></svg>Larkwood, Sk</li>
      </ul>
    </div>
  </section>

  <section class="card card-back" aria-label="Card back">
    <div class="brand-emboss">
      <span class="brand-mark"></span>
      <span class="brand-name">Shine Barn<br>Auto Care</span>
    </div>
    <p class="services">
      complete interior&amp; exterior detail<span class="dot">•</span>paint correction &amp; protection<br>
      ceramic coating<span class="dot">•</span>trim restore<span class="dot">•</span>auto carpet &amp; seat cleaning
    </p>
  </section>

</main>
</body>
</html>
```